Report template for evaluation reports to be used by non designers

We are looking for a report template that meets all the requirements listed in the attached documents. letter head, logo etc have been enclosed. Its important that the colour integrity is kept, but beyond that options are welcome.
Its important that the document is extremely easy to use and that is able to be adapted to include eatables, figures, pictures, text boxes etc and keep the integrity of the template

Target Market(s)

Governments, Civil society organisations and research institutions

Font styles to use
Sans Serif

Colors
6b449b
876aae
c0c0c0
000000

Requirements
Must have
• Clean, professional, not concluded, modern, must be easy to use
Should not have
• too busy, hard to use

```html
<!DOCTYPE html>
<html lang="en">
<head>
<meta charset="utf-8">
<title>Orrenby Institute – Report 2018 Cover</title>
<link href="https://fonts.googleapis.com/css2?family=Montserrat:wght@400;500;600&family=Oswald:wght@700&display=swap" rel="stylesheet">
<style>
  :root {
    --purple: #6b449b;
    --lilac: #876aae;
    --lilac-soft: #a792c8;
    --silver: #c0c0c0;
    --silver-faint: #ececec;
    --ink: #000000;
    --text: #3a3a3a;
    --paper: #ffffff;
    --stage: #d9d9d9;
  }
  * { box-sizing: border-box; margin: 0; padding: 0; }
  html, body { width: 1200px; height: 847px; overflow: hidden; }
  body {
    background: var(--stage);
    font-family: "Montserrat", Arial, sans-serif;
    position: relative;
  }
  .spread {
    position: absolute;
    left: 105px; top: 70px;
    width: 990px; height: 707px;
    display: flex;
  }
  .page {
    position: relative;
    width: 495px; height: 707px;
    background: var(--paper);
    overflow: hidden;
  }
  .back-cover { border-top: 5px solid var(--purple); }
  .front-cover { border-bottom: 5px solid var(--purple); }

  /* back cover */
  .world-map {
    position: absolute;
    left: 20px; top: 90px;
    width: 455px; height: 300px;
    background: radial-gradient(ellipse at 55% 45%, #e6e6e6 0%, #efefef 55%, var(--paper) 80%);
    border-radius: 40px;
  }
  .back-brand {
    position: absolute;
    left: 0; right: 0; top: 478px;
    text-align: center;
  }
  .brand {
    display: inline-flex; align-items: center; gap: 10px;
    font-weight: 500; color: var(--ink);
    letter-spacing: 0.16em; text-transform: uppercase;
    white-space: nowrap;
  }
  .brand-dot {
    display: inline-block; border-radius: 50%;
    background: var(--purple);
    flex: none;
  }
  .back-brand .brand { font-size: 20px; }
  .back-brand .brand-dot { width: 13px; height: 13px; }

  .contacts {
    position: absolute;
    left: 25px; right: 25px; top: 565px;
    display: flex; justify-content: space-between;
  }
  .contact {
    width: 148px; text-align: center;
    font-size: 8.5px; line-height: 1.5; color: var(--text);
  }
  .contact-icon {
    width: 48px; height: 48px; border-radius: 50%;
    margin: 0 auto 10px;
    display: flex; align-items: center; justify-content: center;
  }
  .contact-icon.lilac { background: var(--lilac); }
  .contact-icon.deep { background: var(--purple); }

  /* front cover */
  .report-title {
    position: absolute;
    right: 40px; top: 36px;
    text-align: right;
  }
  .report-title .word {
    font-family: "Oswald", "Arial Narrow", sans-serif;
    font-weight: 700; font-size: 30px; line-height: 1;
    color: var(--purple); letter-spacing: 0.02em;
  }
  .report-title .year {
    font-family: "Montserrat", Arial, sans-serif;
    font-weight: 600; font-size: 22px; line-height: 1.1;
    color: var(--silver); letter-spacing: 0.32em;
  }
  .title-marker { position: absolute; left: 280px; top: 48px; }
  .composition { position: absolute; left: 0; top: 0; }
  .front-brand {
    position: absolute;
    left: 0; right: 0; top: 602px;
    text-align: center;
  }
  .front-brand .brand { font-size: 26px; }
  .front-brand .brand-dot { width: 16px; height: 16px; }
</style>
</head>
<body>
  <main class="spread">
    <section class="page back-cover">
      <div class="world-map" role="img" aria-label="Faint grey world map"></div>

      <div class="back-brand">
        <span class="brand"><span class="brand-dot"></span>Orrenby Institute</span>
      </div>

      <div class="contacts">
        <div class="contact">
          <div class="contact-icon lilac">
            <svg width="22" height="22" viewBox="0 0 22 22" aria-hidden="true">
              <circle cx="11" cy="7" r="4" fill="#fff"/>
              <path d="M3 19c0-4.5 3.6-7 8-7s8 2.5 8 7z" fill="#fff"/>
            </svg>
          </div>
          +64 21 555 0184
        </div>
        <div class="contact">
          <div class="contact-icon lilac">
            <svg width="22" height="22" viewBox="0 0 22 22" aria-hidden="true">
              <circle cx="12.5" cy="9" r="5" fill="none" stroke="#fff" stroke-width="2"/>
              <line x1="9" y1="12.5" x2="4" y2="17.5" stroke="#fff" stroke-width="2.4" stroke-linecap="round"/>
            </svg>
          </div>
          hello@orrenby-institute.example<br>www.orrenby-institute.example
        </div>
        <div class="contact">
          <div class="contact-icon deep">
            <svg width="22" height="22" viewBox="0 0 22 22" aria-hidden="true">
              <path d="M11 3 2 11h3v8h5v-5h2v5h5v-8h3z" fill="#fff"/>
            </svg>
          </div>
          12 Harbour Lane,<br>Kingsford, NZ 4410
        </div>
      </div>
    </section>

    <section class="page front-cover">
      <svg class="title-marker" width="30" height="22" viewBox="0 0 30 22" aria-hidden="true">
        <polygon points="0,0 30,8 12,22" fill="var(--purple)"/>
        <polygon points="12,22 30,8 22,22" fill="var(--lilac-soft)"/>
      </svg>
      <div class="report-title">
        <div class="word">REPORT</div>
        <div class="year">2018</div>
      </div>

      <svg class="composition" width="495" height="707" viewBox="0 0 495 707">
        <defs>
          <linearGradient id="photoTone" x1="0" y1="0" x2="1" y2="1">
            <stop offset="0" stop-color="#c9d6df"/>
            <stop offset="0.5" stop-color="#6d7178"/>
            <stop offset="1" stop-color="#2e3035"/>
          </linearGradient>
        </defs>
        <circle cx="400" cy="560" r="120" fill="none" stroke="var(--silver-faint)" stroke-width="30"/>
        <line x1="40" y1="90" x2="440" y2="290" stroke="#e4e4e4" stroke-width="1"/>
        <line x1="240" y1="90" x2="460" y2="260" stroke="#e4e4e4" stroke-width="1"/>
        <g transform="translate(250 300) rotate(30)">
          <rect x="-190" y="-100" width="60" height="60" fill="var(--lilac)" transform="rotate(8)"/>
          <rect x="-95" y="-95" width="190" height="190" fill="var(--lilac-soft)"/>
          <polygon points="-95,-95 -95,95 -65,65 -65,-65" fill="var(--purple)"/>
          <polygon points="-95,-95 95,-95 65,-65 -65,-65" fill="var(--lilac)"/>
          <rect x="-65" y="-65" width="130" height="130" fill="var(--paper)"/>
          <rect x="110" y="-40" width="62" height="62" fill="var(--lilac)"/>
          <rect x="-40" y="120" width="50" height="50" fill="var(--silver)"/>
          <rect x="-58" y="-58" width="116" height="116" fill="url(#photoTone)" role="img" aria-label="Photo of a city office tower"/>
        </g>
        <text x="250" y="311" text-anchor="middle" font-family="Montserrat, Arial, sans-serif" font-weight="600" font-size="30" fill="#fff" transform="rotate(-8 250 300)">Image</text>
      </svg>

      <div class="front-brand">
        <span class="brand"><span class="brand-dot"></span>Orrenby Institute</span>
      </div>
    </section>
  </main>
</body>
</html>
```